We are a team of QNV cloud specialists who obsessively empower customer organisations to feel confident in managing their growing QNV use, whatever their business needs are. As leading edge cloud artisans we do this by using our passion for simplification, reuse, automation, innovation and quality. We always put the 'customer journey' at the center of our many obsessions.

Target Market(s)

It's mainly a corporate market and we are targeting medium-sized businesses.

Industry/Entity Type

It Company

Contact Information for Business Card

Company name: Corvexo
Name
position
Phone
Web
Email

Font styles to use
Serif
Decorative

Colors

Designer to choose colors to be used in the design.

Requirements
Must have
• Must be funky and modern.
Nice to have
• Preferably embossed.

```html
<!DOCTYPE html>
<html lang="en">
<head>
<meta charset="utf-8">
<title>Corvexo Business Card</title>
<link rel="stylesheet" href="https://fonts.googleapis.com/css2?family=Open+Sans:wght@400;600;700&display=swap">
<style>
  :root {
    --canvas: #e4ddd2;
    --card-white: #ffffff;
    --sky: #3fb2ec;
    --sky-deep: #1f9ad8;
    --orange: #f47a20;
    --ink: #0b0b0b;
    --ink-soft: #1c1c1c;
    --text-light: #ffffff;
    --shadow: rgba(40, 30, 15, 0.28);
  }
  * { box-sizing: border-box; margin: 0; padding: 0; }
  html, body {
    width: 1200px;
    height: 1024px;
    overflow: hidden;
    background: var(--canvas);
    font-family: "Open Sans", Arial, sans-serif;
  }
  .canvas {
    position: relative;
    width: 1200px;
    height: 1024px;
  }
  .card {
    position: absolute;
    left: 215px;
    width: 770px;
    height: 440px;
    border-radius: 4px;
    overflow: hidden;
    box-shadow: 0 14px 30px var(--shadow);
  }
  /* Front */
  .card-front {
    top: 52px;
    background: var(--card-white);
  }
  .front-band {
    position: absolute;
    left: 0;
    right: 0;
    bottom: 0;
    height: 200px;
    background: var(--sky);
  }
  .front-end {
    position: absolute;
    top: 0;
    right: 0;
    width: 170px;
    height: 100%;
    background: var(--sky);
  }
  .front-brand {
    position: absolute;
    left: 70px;
    top: 92px;
    display: flex;
    align-items: center;
    gap: 18px;
  }
  .brand-dot {
    width: 34px;
    height: 34px;
    border-radius: 50%;
    background: var(--sky);
    flex: none;
  }
  .brand-name {
    font-family: "Open Sans", Arial, sans-serif;
    font-weight: 600;
    color: var(--orange);
    font-size: 58px;
    letter-spacing: 10px;
    line-height: 1;
    text-transform: uppercase;
  }
  .contact {
    position: absolute;
    left: 70px;
    bottom: 34px;
    color: var(--text-light);
  }
  .contact-name {
    font-weight: 700;
    font-size: 30px;
    letter-spacing: 1px;
    text-transform: uppercase;
    line-height: 1.1;
  }
  .contact-role {
    font-weight: 600;
    font-size: 24px;
    margin-bottom: 14px;
  }
  .contact-list { list-style: none; }
  .contact-list li {
    display: flex;
    align-items: center;
    gap: 10px;
    font-size: 19px;
    line-height: 1.55;
  }
  .contact-list svg { width: 18px; height: 18px; flex: none; }
  /* Back */
  .card-back {
    top: 532px;
    background: linear-gradient(150deg, var(--ink-soft) 0%, var(--ink) 55%, #000 100%);
  }
  .back-brand {
    position: absolute;
    left: 50%;
    top: 150px;
    transform: translateX(-50%);
    display: flex;
    align-items: center;
    gap: 18px;
  }
  .back-web {
    position: absolute;
    left: 60px;
    bottom: 46px;
    color: var(--text-light);
    font-size: 18px;
    letter-spacing: 0.5px;
  }
  .back-web .accent { color: var(--orange); }
</style>
</head>
<body>
<main class="canvas">
  <section class="card card-front" aria-label="Business card front">
    <div class="front-band"></div>
    <div class="front-end"></div>
    <div class="front-brand">
      <span class="brand-dot"></span>
      <span class="brand-name">Corvexo</span>
    </div>
    <div class="contact">
      <p class="contact-name">Marcus Hale</p>
      <p class="contact-role">Position</p>
      <ul class="contact-list">
        <li>
          <svg viewBox="0 0 24 24" aria-hidden="true"><path fill="#fff" d="M6.6 10.8a15.1 15.1 0 0 0 6.6 6.6l2.2-2.2a1 1 0 0 1 1-.25 11.4 11.4 0 0 0 3.6.57 1 1 0 0 1 1 1V20a1 1 0 0 1-1 1A17 17 0 0 1 3 4a1 1 0 0 1 1-1h3.5a1 1 0 0 1 1 1c0 1.25.2 2.45.57 3.57a1 1 0 0 1-.25 1z"/></svg>
          0400 118 275
        </li>
        <li>
          <svg viewBox="0 0 24 24" aria-hidden="true"><rect x="2" y="5" width="20" height="14" rx="1.5" fill="#fff"/><path d="M3 6.5l9 6.5 9-6.5" fill="none" stroke="#3fb2ec" stroke-width="1.8"/></svg>
          marcus@corvexo.com
        </li>
        <li>
          <svg viewBox="0 0 24 24" aria-hidden="true"><circle cx="12" cy="12" r="9.5" fill="none" stroke="#fff" stroke-width="1.8"/><ellipse cx="12" cy="12" rx="4" ry="9.5" fill="none" stroke="#fff" stroke-width="1.5"/><path d="M2.5 12h19" stroke="#fff" stroke-width="1.5"/></svg>
          www.corvexo.com
        </li>
      </ul>
    </div>
  </section>

  <section class="card card-back" aria-label="Business card back">
    <div class="back-brand">
      <span class="brand-dot"></span>
      <span class="brand-name">Corvexo</span>
    </div>
    <p class="back-web">www.<span class="accent">corvexo</span>.com</p>
  </section>
</main>
</body>
</html>
```